Can Design for Fun, Growing Health Food Brand

We are launching a brand new product, electrolyte seltzer drinks. We want the design to be clean/simple and slightly modern while staying true to our brand identity. Must say "Mineral Hydration" as the product descriptor, sub headline is "Carbonated electrolyte beverage with sea moss and real fruit juice". First flavors will be Watermelon Mint and Mango.

Target Market(s)

Women ages 30-50 who are interested in health wellness/trends

Industry/Entity Type

Health & Wellness

Font styles to use
Sans Serif

Requirements
Must have
• Tall, skinny can, current Bright Kelp Co Logo, use aluminum on can as element in design.
Nice to have
• Be fun, clean and modern. Would like to see the label less busy than our gels.
Should not have
• Avoid putting flavor on bottom 1/5 of can. No gradient color changes. Do not want really detailed or realistic fruit image, prefer drawings or similar.

```html
<!DOCTYPE html>
<html lang="en">
<head>
<meta charset="utf-8">
<title>Bright Kelp Co – Mineral Hydration Cans</title>
<link rel="stylesheet" href="https://fonts.googleapis.com/css2?family=Barlow:wght@600;700&family=Barlow+Semi+Condensed:wght@400;500;600&display=swap">
<style>
  :root {
    --backdrop: #efe4d4;
    --label-white: #f5f4f1;
    --brand-green: #1c4a3a;
    --ink: #1f3d33;
    --aluminum-light: #e4e5e6;
    --aluminum-dark: #b9bcbf;
    --watermelon: #ec6a6d;
    --watermelon-deep: #d9484f;
    --watermelon-rind: #2f6b3f;
    --mango: #f3bc2d;
    --mango-deep: #e49a17;
    --white: #ffffff;
  }
  * { margin: 0; padding: 0; box-sizing: border-box; }
  html, body { width: 1200px; height: 1164px; overflow: hidden; }
  body {
    background: var(--backdrop);
    font-family: "Barlow Semi Condensed", sans-serif;
    color: var(--ink);
    position: relative;
  }
  .can-label {
    position: absolute;
    top: 60px;
    width: 380px;
    height: 1044px;
    background: var(--label-white);
    overflow: hidden;
    border-radius: 6px;
  }
  .can-label--watermelon { left: 150px; --flavor: var(--watermelon); --accent: var(--watermelon-deep); }
  .can-label--mango { left: 670px; --flavor: var(--mango); --accent: var(--mango-deep); }

  .aluminum-rim {
    position: absolute; left: 0; right: 0; height: 20px;
    background: linear-gradient(180deg, var(--aluminum-light), var(--aluminum-dark));
    z-index: 3;
  }
  .aluminum-rim--top { top: 0; }
  .aluminum-rim--bottom { bottom: 0; }

  .brand-tab {
    position: absolute; left: 50%; top: 20px;
    width: 94px; height: 140px; margin-left: -47px;
    background: var(--brand-green);
    border-radius: 0 0 47px 47px;
    display: flex; align-items: flex-end; justify-content: center;
    padding-bottom: 20px;
  }
  .brand-tab__circle {
    width: 60px; height: 60px; border-radius: 50%;
    border: 3px solid var(--label-white);
  }
  .brand-name {
    position: absolute; top: 190px; left: 0; right: 0;
    text-align: center; font-weight: 600; font-size: 26px;
    letter-spacing: 2.5px; color: var(--brand-green);
  }
  .divider {
    position: absolute; top: 236px; left: 50%;
    width: 108px; margin-left: -54px; height: 8px;
  }
  .product-title {
    position: absolute; top: 262px; left: 0; right: 0;
    text-align: center;
    font-family: "Barlow", sans-serif; font-weight: 700;
    font-size: 60px; line-height: 1.0; color: var(--brand-green);
    letter-spacing: -0.5px;
  }
  .product-subtitle {
    position: absolute; top: 400px; left: 0; right: 0;
    text-align: center; font-size: 20px; line-height: 1.3;
    font-weight: 500; color: var(--ink);
  }
  .benefits {
    position: absolute; top: 488px; left: 30px; right: 30px;
    display: flex; justify-content: space-between;
    list-style: none;
  }
  .benefit {
    width: 100px; text-align: center;
    font-size: 14px; font-weight: 500; line-height: 1.25;
    text-transform: uppercase; color: var(--ink);
  }
  .benefit svg { display: block; margin: 0 auto 8px; }

  .flavor-band {
    position: absolute; left: 0; top: 596px; width: 380px; height: 448px;
  }
  .flavor-name {
    position: absolute; top: 672px; left: 0; right: 0;
    text-align: center; color: var(--white);
    font-weight: 600; font-size: 40px; line-height: 1.0; letter-spacing: 1.5px;
  }
  .can-label--mango .flavor-name { top: 692px; }
  .fruit-art {
    position: absolute; left: 80px; top: 770px; width: 220px; height: 180px;
    border-radius: 50%;
  }
  .can-label--watermelon .fruit-art {
    background: radial-gradient(circle at 45% 45%, #f27d80 0%, var(--watermelon-deep) 60%, var(--watermelon-rind) 100%);
  }
  .can-label--mango .fruit-art {
    background: radial-gradient(circle at 45% 45%, #fbd060 0%, var(--mango-deep) 70%, #3f7d3a 100%);
  }
  .volume {
    position: absolute; top: 978px; left: 0; right: 0;
    text-align: center; font-size: 20px; font-weight: 500; color: var(--ink);
  }
</style>
</head>
<body>

<article class="can-label can-label--watermelon">
  <div class="aluminum-rim aluminum-rim--top"></div>
  <div class="brand-tab"><span class="brand-tab__circle"></span></div>
  <p class="brand-name">BRIGHT KELP CO</p>
  <svg class="divider" viewBox="0 0 108 8"><line x1="0" y1="4" x2="44" y2="4" stroke="var(--watermelon-deep)" stroke-width="1.5"/><circle cx="54" cy="4" r="4" fill="var(--watermelon-deep)"/><line x1="64" y1="4" x2="108" y2="4" stroke="var(--watermelon-deep)" stroke-width="1.5"/></svg>
  <h1 class="product-title">Mineral<br>Hydration</h1>
  <p class="product-subtitle">Carbonated electrolyte<br>beverage with sea moss<br>and real fruit juice</p>
  <ul class="benefits">
    <li class="benefit"><svg width="44" height="44" viewBox="0 0 44 44"><circle cx="22" cy="22" r="20" fill="none" stroke="var(--brand-green)" stroke-width="2"/><circle cx="22" cy="22" r="8" fill="none" stroke="var(--brand-green)" stroke-width="2"/></svg>Sea Moss<br>Power</li>
    <li class="benefit"><svg width="44" height="44" viewBox="0 0 44 44"><circle cx="22" cy="22" r="20" fill="none" stroke="var(--brand-green)" stroke-width="2"/><path d="M22 11 L32 16.5 V27.5 L22 33 L12 27.5 V16.5 Z M12 16.5 L22 22 L32 16.5 M22 22 V33" fill="none" stroke="var(--brand-green)" stroke-width="2" stroke-linejoin="round"/></svg>Essential<br>Minerals</li>
    <li class="benefit"><svg width="44" height="44" viewBox="0 0 44 44"><circle cx="22" cy="22" r="20" fill="none" stroke="var(--brand-green)" stroke-width="2"/><path d="M22 11 C26 17 29 21 29 25 A7 7 0 0 1 15 25 C15 21 18 17 22 11 Z" fill="none" stroke="var(--brand-green)" stroke-width="2"/></svg>No Added<br>Sugar</li>
  </ul>
  <svg class="flavor-band" viewBox="0 0 380 448" preserveAspectRatio="none"><path d="M0 50 C 80 70, 190 70, 270 35 C 320 15, 350 8, 380 0 V448 H0 Z" fill="var(--flavor)"/><path d="M10 170 C 80 150, 140 180, 200 165" fill="none" stroke="var(--white)" stroke-width="2" opacity="0.7"/></svg>
  <h2 class="flavor-name">WATERMELON<br>MINT</h2>
  <div class="fruit-art" role="img" aria-label="Drawn watermelon slice with mint leaves"></div>
  <p class="volume">12 FL OZ (355 mL)</p>
  <div class="aluminum-rim aluminum-rim--bottom"></div>
</article>

<article class="can-label can-label--mango">
  <div class="aluminum-rim aluminum-rim--top"></div>
  <div class="brand-tab"><span class="brand-tab__circle"></span></div>
  <p class="brand-name">BRIGHT KELP CO</p>
  <svg class="divider" viewBox="0 0 108 8"><line x1="0" y1="4" x2="44" y2="4" stroke="var(--mango-deep)" stroke-width="1.5"/><circle cx="54" cy="4" r="4" fill="var(--mango-deep)"/><line x1="64" y1="4" x2="108" y2="4" stroke="var(--mango-deep)" stroke-width="1.5"/></svg>
  <h1 class="product-title">Mineral<br>Hydration</h1>
  <p class="product-subtitle">Carbonated electrolyte<br>beverage with sea moss<br>and real fruit juice</p>
  <ul class="benefits">
    <li class="benefit"><svg width="44" height="44" viewBox="0 0 44 44"><circle cx="22" cy="22" r="20" fill="none" stroke="var(--brand-green)" stroke-width="2"/><circle cx="22" cy="22" r="8" fill="none" stroke="var(--brand-green)" stroke-width="2"/></svg>Sea Moss<br>Power</li>
    <li class="benefit"><svg width="44" height="44" viewBox="0 0 44 44"><circle cx="22" cy="22" r="20" fill="none" stroke="var(--brand-green)" stroke-width="2"/><path d="M22 11 L32 16.5 V27.5 L22 33 L12 27.5 V16.5 Z M12 16.5 L22 22 L32 16.5 M22 22 V33" fill="none" stroke="var(--brand-green)" stroke-width="2" stroke-linejoin="round"/></svg>Essential<br>Minerals</li>
    <li class="benefit"><svg width="44" height="44" viewBox="0 0 44 44"><circle cx="22" cy="22" r="20" fill="none" stroke="var(--brand-green)" stroke-width="2"/><path d="M22 11 C26 17 29 21 29 25 A7 7 0 0 1 15 25 C15 21 18 17 22 11 Z" fill="none" stroke="var(--brand-green)" stroke-width="2"/></svg>No Added<br>Sugar</li>
  </ul>
  <svg class="flavor-band" viewBox="0 0 380 448" preserveAspectRatio="none"><path d="M0 50 C 80 70, 190 70, 270 35 C 320 15, 350 8, 380 0 V448 H0 Z" fill="var(--flavor)"/><path d="M10 170 C 80 150, 140 180, 200 165" fill="none" stroke="var(--white)" stroke-width="2" opacity="0.7"/></svg>
  <h2 class="flavor-name">MANGO</h2>
  <div class="fruit-art" role="img" aria-label="Drawn whole mango with leaves and a cubed mango half"></div>
  <p class="volume">12 FL OZ (355 mL)</p>
  <div class="aluminum-rim aluminum-rim--bottom"></div>
</article>

</body>
</html>
```